Promotion Layer (UI Design)

What we need is not a classical App Design.
We need a UI Design for a SDK, which appears as Layer in different apps.
The layer will contain a list/library which will show cool goodies for the app user.

The attached file will give you all the details you need to start.

Note: The Screenshots do show app content. But these are just place holders.
The content is NOT part of the design task. Because we just provide the layer...

The crucial part of this task is, to create a UI design, that is stylish, simple and does not harm the 3rd party app, where it will be showed. While you design it, allways try to think "do I like this, when it appears in my own app"

Your files should be made in the right size/dimensions of ios.

Industry/Entity Type

Library

Font styles to use
Sans Serif

Requirements
Must have
• Must fit the iOS 7 Style

```html
<!DOCTYPE html>
<html lang="de">
<head>
<meta charset="utf-8">
<title>Promotion Layer – Neue Angebote</title>
<link rel="stylesheet" href="https://fonts.googleapis.com/css2?family=Mulish:wght@300;400;700&display=swap">
<style>
  :root {
    --stage: #ffffd6;
    --screen-bg: #f3f1ef;
    --card: #ffffff;
    --card-border: #e2e0de;
    --title: #a9a9a9;
    --count: #b4b4b4;
    --heart: #f47896;
    --tab-bg: #ffffff;
    --tab-border: #d6d6d6;
    --icon-grey: #8c8c8c;
    --icon-blue: #4fb0e4;
    --label: #6a6a6a;
  }
  * { box-sizing: border-box; margin: 0; padding: 0; }
  html, body {
    width: 1200px; height: 2282px; overflow: hidden;
    background: var(--stage);
    font-family: "Mulish", "Helvetica Neue", Arial, sans-serif;
  }
  .stage { position: relative; width: 1200px; height: 2282px; }

  .screen {
    position: absolute; left: 0; width: 600px; height: 1022px;
    background: var(--screen-bg); overflow: hidden;
  }
  .screen--closed { top: 43px; }
  .screen--open { top: 1159px; }

  .header-band {
    position: absolute; left: 0; top: 0; width: 600px; height: 34px;
    background: linear-gradient(90deg, #8a3f5a 0%, #b25a6a 25%, #6e3a63 55%, #8d4b6c 80%, #5e2c50 100%);
  }

  .card {
    position: absolute; left: 47px; width: 547px;
    background: var(--card); border: 1px solid var(--card-border);
    box-shadow: 0 2px 4px rgba(0,0,0,0.08);
  }
  .card--first { top: 90px; height: 488px; }
  .card--second { top: 664px; height: 420px; }
  .card__media {
    position: absolute; left: 20px; top: 19px; width: 507px; height: 347px;
  }
  .card__media--statue {
    background: linear-gradient(180deg, #6f9ddc 0%, #a9c6ee 45%, #5f6a70 70%, #4e5356 100%);
  }
  .card__media--fishbowl {
    background: radial-gradient(ellipse at 55% 65%, #8fe0ff 0%, #3aa7e0 35%, #1d3f9c 75%, #1c2a78 100%);
    height: 400px;
  }
  .card__footer {
    position: absolute; left: 20px; right: 20px; top: 366px; height: 122px;
    display: flex; align-items: center; justify-content: space-between;
  }
  .card__title { font-weight: 300; font-size: 38px; color: var(--title); letter-spacing: 0.2px; margin-top: -12px; }
  .card__likes { display: flex; align-items: center; gap: 14px; margin-top: -12px; margin-right: 8px; }
  .card__count { font-weight: 300; font-size: 32px; color: var(--count); }
  .card__heart { width: 42px; height: 38px; }

  .promo-tab {
    position: absolute; top: 371px; width: 116px; height: 240px;
    display: flex; background: var(--tab-bg); border: 1px solid var(--tab-border);
  }
  .screen--open .promo-tab { left: -45px; }
  .screen--closed .promo-tab { left: 0; }
  .promo-tab__icons { width: 79px; display: flex; flex-direction: column; border-right: 1px solid var(--tab-border); }
  .promo-tab__icon {
    flex: 1; display: flex; align-items: center; justify-content: center;
    border-bottom: 1px solid var(--tab-border);
  }
  .promo-tab__icon:last-child { border-bottom: none; }
  .promo-tab__icon svg { width: 56px; height: 62px; }
  .promo-tab__label {
    position: relative; flex: 1;
  }
  .promo-tab__text {
    position: absolute; left: 50%; top: 104px;
    transform: translate(-50%, -50%) rotate(-90deg);
    white-space: nowrap; font-weight: 700; font-size: 19px; letter-spacing: 0.5px; color: var(--label);
  }
  .promo-tab__arrow { position: absolute; left: 6px; bottom: 6px; width: 24px; height: 24px; }
</style>
</head>
<body>
<main class="stage">

  <section class="screen screen--closed">
    <div class="header-band"></div>
    <article class="card card--first">
      <div class="card__media card__media--statue" role="img" aria-label="Photo of a stone statue against a blue cloudy sky"></div>
      <div class="card__footer">
        <span class="card__title">Suryavanan</span>
        <span class="card__likes">
          <span class="card__count">11</span>
          <svg class="card__heart" viewBox="0 0 24 22"><path fill="var(--heart)" d="M12 21.5 2.6 12.4C-.3 9.5.2 4.6 3.6 2.6 6.3 1 9.8 1.8 12 4.3c2.2-2.5 5.7-3.3 8.4-1.7 3.4 2 3.9 6.9 1 9.8Z"/></svg>
        </span>
      </div>
    </article>
    <article class="card card--second">
      <div class="card__media card__media--fishbowl" role="img" aria-label="Illustration of a fish leaping out of a glass fishbowl"></div>
    </article>
    <aside class="promo-tab">
      <div class="promo-tab__icons">
        <div class="promo-tab__icon">
          <svg viewBox="0 0 28 32"><rect x="9" y="2" width="10" height="28" rx="3" fill="none" stroke="var(--icon-blue)" stroke-width="1.6"/><circle cx="14" cy="9" r="2.2" fill="none" stroke="var(--icon-blue)" stroke-width="1.6"/></svg>
        </div>
        <div class="promo-tab__icon">
          <svg viewBox="0 0 28 32"><path d="M3 15h5v13H3zM8 16l5-8c.6-2 1-4 2.5-4 2 0 2 2.5 1.4 5L16 13h7c1.8 0 2.6 1.6 2.2 3l-2.5 9.5C22.3 27 21.4 28 20 28H8" fill="none" stroke="var(--icon-grey)" stroke-width="1.6" stroke-linejoin="round"/></svg>
        </div>
        <div class="promo-tab__icon">
          <svg viewBox="0 0 28 32"><rect x="7" y="2" width="14" height="28" rx="2.5" fill="none" stroke="var(--icon-grey)" stroke-width="1.6"/><line x1="7" y1="7" x2="21" y2="7" stroke="var(--icon-grey)" stroke-width="1.4"/><line x1="7" y1="24" x2="21" y2="24" stroke="var(--icon-grey)" stroke-width="1.4"/><circle cx="14" cy="27" r="1.2" fill="var(--icon-grey)"/></svg>
        </div>
      </div>
      <div class="promo-tab__label">
        <span class="promo-tab__text">NEUE ANGEBOTE</span>
        <svg class="promo-tab__arrow" viewBox="0 0 12 12"><path d="M1 1l10 10M11 4v7H4" fill="none" stroke="var(--label)" stroke-width="1.3"/></svg>
      </div>
    </aside>
  </section>

  <section class="screen screen--open">
    <div class="header-band"></div>
    <article class="card card--first">
      <div class="card__media card__media--statue" role="img" aria-label="Photo of a stone statue against a blue cloudy sky"></div>
      <div class="card__footer">
        <span class="card__title">Suryavanan</span>
        <span class="card__likes">
          <span class="card__count">11</span>
          <svg class="card__heart" viewBox="0 0 24 22"><path fill="var(--heart)" d="M12 21.5 2.6 12.4C-.3 9.5.2 4.6 3.6 2.6 6.3 1 9.8 1.8 12 4.3c2.2-2.5 5.7-3.3 8.4-1.7 3.4 2 3.9 6.9 1 9.8Z"/></svg>
        </span>
      </div>
    </article>
    <article class="card card--second">
      <div class="card__media card__media--fishbowl" role="img" aria-label="Illustration of a fish leaping out of a glass fishbowl"></div>
    </article>
    <aside class="promo-tab">
      <div class="promo-tab__icons">
        <div class="promo-tab__icon">
          <svg viewBox="0 0 28 32"><rect x="9" y="2" width="10" height="28" rx="3" fill="none" stroke="var(--icon-blue)" stroke-width="1.6"/><circle cx="14" cy="9" r="2.2" fill="none" stroke="var(--icon-blue)" stroke-width="1.6"/></svg>
        </div>
        <div class="promo-tab__icon">
          <svg viewBox="0 0 28 32"><path d="M3 15h5v13H3zM8 16l5-8c.6-2 1-4 2.5-4 2 0 2 2.5 1.4 5L16 13h7c1.8 0 2.6 1.6 2.2 3l-2.5 9.5C22.3 27 21.4 28 20 28H8" fill="none" stroke="var(--icon-grey)" stroke-width="1.6" stroke-linejoin="round"/></svg>
        </div>
        <div class="promo-tab__icon">
          <svg viewBox="0 0 28 32"><rect x="7" y="2" width="14" height="28" rx="2.5" fill="none" stroke="var(--icon-grey)" stroke-width="1.6"/><line x1="7" y1="7" x2="21" y2="7" stroke="var(--icon-grey)" stroke-width="1.4"/><line x1="7" y1="24" x2="21" y2="24" stroke="var(--icon-grey)" stroke-width="1.4"/><circle cx="14" cy="27" r="1.2" fill="var(--icon-grey)"/></svg>
        </div>
      </div>
      <div class="promo-tab__label">
        <span class="promo-tab__text">NEUE ANGEBOTE</span>
        <svg class="promo-tab__arrow" viewBox="0 0 12 12"><path d="M1 1l10 10M11 4v7H4" fill="none" stroke="var(--label)" stroke-width="1.3"/></svg>
      </div>
    </aside>
  </section>

</main>
</body>
</html>
```